Business Card Design Project 4 Construction Business

I am after a creative, but sleek and simple/ clean business card design. This design will form the basis of future items and might include a logo or simply a creative way to lay out the text of my company name 'kestrel ventures'
I like the simplicity of black and white however I would also be happy to see a splash of colour introduced somehow to give the text some interest and make it stand out.
I would like a double sided card.
I am young (ish!) and professional, offering construction and project management services, what I don't want is the traditional builders type card featuring a cheesy hammer/ saw image etc.
As the company name, kestrel ventures, suggests, we focus on working closely and collaboratively together, in synergy with all stakeholders involved in the projects that we undertake
Construction

```html
<!DOCTYPE html>
<html lang="en">
<head>
<meta charset="utf-8">
<title>Kestrel Ventures — Business Card</title>
<link rel="stylesheet" href="https://fonts.googleapis.com/css2?family=Roboto:wght@300;400;500&display=swap">
<style>
  :root {
    --backdrop: #2e3231;
    --paper: #f4f4f2;
    --charcoal: #3d3e41;
    --charcoal-deep: #343538;
    --accent: #e0453a;
    --ink: #333436;
    --muted: #a9aaad;
    --rule: #8c8d90;
    --light-text: #e6e6e6;
  }
  * { box-sizing: border-box; margin: 0; padding: 0; }
  html, body {
    width: 1200px;
    height: 900px;
    overflow: hidden;
    background: var(--backdrop);
    font-family: "Roboto", Arial, sans-serif;
  }
  .canvas {
    width: 1200px;
    height: 900px;
    display: flex;
    flex-direction: column;
    align-items: center;
    justify-content: center;
    gap: 60px;
  }
  .card {
    position: relative;
    width: 620px;
    height: 379px;
    display: flex;
    overflow: hidden;
    box-shadow: 0 10px 30px rgba(0,0,0,0.35);
  }
  .card__brand-panel {
    position: relative;
    width: 270px;
    background: var(--paper);
    display: flex;
    align-items: center;
    justify-content: center;
  }
  .card--front .card__brand-panel {
    border-left: 9px solid var(--accent);
  }
  .card__info-panel {
    position: relative;
    flex: 1;
    background: linear-gradient(180deg, var(--charcoal) 0%, var(--charcoal-deep) 100%);
  }
  .card__accent-line {
    position: absolute;
    left: 0;
    width: 3px;
    bottom: 0;
    background: var(--accent);
  }
  .card--front .card__accent-line { top: 96px; }
  .card--back .card__accent-line { top: 192px; }

  .wordmark {
    display: flex;
    align-items: flex-start;
    gap: 10px;
    color: var(--ink);
    font-weight: 500;
    line-height: 1;
  }
  .wordmark__dot {
    width: 16px;
    height: 16px;
    border-radius: 50%;
    background: var(--accent);
    margin-top: 6px;
    flex-shrink: 0;
  }
  .wordmark__name {
    display: flex;
    flex-direction: column;
    gap: 6px;
  }
  .wordmark__primary { font-size: 34px; letter-spacing: -0.5px; }
  .wordmark__secondary { font-size: 20px; padding-left: 40px; }

  .person {
    position: absolute;
    left: 34px;
    top: 40px;
  }
  .person__name {
    color: var(--accent);
    font-size: 21px;
    font-weight: 300;
  }
  .person__role {
    color: var(--muted);
    font-size: 11px;
    font-weight: 300;
    margin-top: 6px;
  }
  .info-rule {
    position: absolute;
    left: 3px;
    right: 0;
    height: 1px;
    background: var(--rule);
  }
  .card--front .info-rule { top: 96px; }
  .card--back .info-rule { top: 192px; }

  .contacts {
    position: absolute;
    left: 34px;
    bottom: 40px;
    display: grid;
    grid-template-columns: 38px auto;
    row-gap: 5px;
    color: var(--light-text);
    font-size: 11.5px;
    font-weight: 300;
  }
  .contacts dt { color: var(--light-text); }

  .website {
    position: absolute;
    left: 26px;
    top: 168px;
    color: var(--light-text);
    font-size: 13.5px;
    font-weight: 300;
    letter-spacing: 0.2px;
  }
</style>
</head>
<body>
<main class="canvas">

  <section class="card card--front" aria-label="Business card front">
    <div class="card__brand-panel">
      <div class="wordmark">
        <span class="wordmark__dot"></span>
        <span class="wordmark__name">
          <span class="wordmark__primary">Kestrel</span>
          <span class="wordmark__secondary">Ventures</span>
        </span>
      </div>
    </div>
    <div class="card__info-panel">
      <span class="card__accent-line"></span>
      <div class="person">
        <p class="person__name">Owen Harcourt</p>
        <p class="person__role">Director</p>
      </div>
      <span class="info-rule"></span>
      <dl class="contacts">
        <dt>T:</dt><dd>0400 555 018</dd>
        <dt>E:</dt><dd>o.harcourt@kestrelventures.com.au</dd>
        <dt>W:</dt><dd>www.kestrelventures.com.au</dd>
        <dt>A:</dt><dd>14 Ferris Lane Chatswood NSW 2067</dd>
      </dl>
    </div>
  </section>

  <section class="card card--back" aria-label="Business card back">
    <div class="card__brand-panel">
      <div class="wordmark">
        <span class="wordmark__dot"></span>
        <span class="wordmark__name">
          <span class="wordmark__primary">Kestrel</span>
          <span class="wordmark__secondary">Ventures</span>
        </span>
      </div>
    </div>
    <div class="card__info-panel">
      <span class="card__accent-line"></span>
      <p class="website">www.kestrelventures.com.au</p>
      <span class="info-rule"></span>
    </div>
  </section>

</main>
</body>
</html>
```